Bluestone Advisory & Mgmt - Professional Business Cards

Hi!

I am a Real Estate Developer and Construction Consultant.

I have a lot of inspiration from previous designs and would be open to using the attached Designs as a starting point. I would like to see these styles incorporated into your designs.

I really need professional business card to go with it that includes my important info.

Look forward to seeing your designs!.

Target Market(s)

My Target market are building owners, lawyers, consultants.

Industry/Entity Type

Real Estate Development

Contact Information for Business Card

My Name: Dorian Pelkey
My Title: Principle
Company Name: Bluestone Advisory & Mgmt, LLC
Address: 348 West 71st Street, 9th FL New York, NY 10010
Mobile: 917.806.3971
Website: bam-hvx.example

Font styles to use
Serif
Sans Serif

Colors

Designer to choose colors to be used in the design.

Requirements
Must have
• Must incorporate the logo attached or have new that looks similar.
• Must use professional font that will be seen and judged by wealthy land owners and developers.
• Must incorporate some of the color green.
Should not have
• Photo's or pictures of people or buildings of any kind.

```html
<!DOCTYPE html>
<html lang="en">
<head>
<meta charset="utf-8">
<title>Bluestone Advisory &amp; Mgmt – Business Cards</title>
<link rel="stylesheet" href="https://fonts.googleapis.com/css2?family=Lato:wght@700&family=Arimo:wght@400&family=Raleway:wght@500;600&display=swap">
<style>
  :root {
    --green: #3fae6a;
    --green-light: #4fb87a;
    --green-dark: #33a35f;
    --ink: #141414;
    --text: #3b3b3b;
    --ring: #f6f4f4;
    --paper: #ffffff;
  }
  * { margin: 0; padding: 0; box-sizing: border-box; }
  html, body {
    width: 1021px; height: 1200px; overflow: hidden;
    background: var(--paper);
  }
  .stage { position: relative; width: 1021px; height: 1200px; }

  .card {
    position: absolute; left: 79px; width: 864px; height: 512px;
    overflow: hidden; background: var(--paper);
    box-shadow: 0 1px 6px rgba(0,0,0,0.18);
  }
  .card--front {
    top: 59px;
    background: linear-gradient(200deg, var(--green-light), var(--green-dark));
  }
  .card--back { top: 613px; }

  .front-panel {
    position: absolute; left: 32px; top: 32px; right: 32px; bottom: 32px;
    background: var(--paper); overflow: hidden;
  }
  .decor { position: absolute; inset: 0; }

  .wordmark {
    position: absolute;
    font-family: "Raleway", sans-serif; font-weight: 600;
    color: var(--green);
    line-height: 1;
  }
  .wordmark--front { left: 138px; top: 120px; }
  .wordmark--front .wordmark-line1 { display: block; font-size: 104px; letter-spacing: -1px; }
  .wordmark--front .wordmark-line2 { display: block; font-size: 50px; margin-top: 22px; }

  .wordmark--back {
    right: 50px; top: 352px; text-align: left; color: var(--paper);
    font-weight: 500;
  }
  .wordmark--back .wordmark-line1 { display: block; font-size: 56px; }
  .wordmark--back .wordmark-line2 { display: block; font-size: 24px; margin-top: 8px; }

  .holder { position: absolute; left: 48px; top: 40px; }
  .holder-name {
    font-family: "Lato", sans-serif; font-weight: 700;
    font-size: 42px; color: var(--ink); letter-spacing: 0.5px; line-height: 1;
  }
  .holder-title {
    font-family: "Arimo", sans-serif; font-size: 23px;
    letter-spacing: 7px; color: var(--text); margin-top: 14px;
  }

  .contact-list { position: absolute; left: 47px; top: 167px; list-style: none; }
  .contact-item { position: absolute; left: 0; display: flex; align-items: flex-start; white-space: nowrap; }
  .contact-item:nth-child(1) { top: 0; }
  .contact-item:nth-child(2) { top: 61px; }
  .contact-item:nth-child(3) { top: 126px; }
  .contact-item:nth-child(4) { top: 191px; }
  .contact-icon {
    width: 44px; height: 44px; border: 1.5px solid var(--green);
    display: flex; align-items: center; justify-content: center; flex: none;
  }
  .contact-icon svg { width: 20px; height: 20px; fill: var(--green); }
  .contact-text {
    font-family: "Arimo", sans-serif; font-size: 25px; color: var(--text);
    margin-left: 23px; line-height: 38px; margin-top: 3px; letter-spacing: 0.8px;
  }
</style>
</head>
<body>
<div class="stage">

  <section class="card card--front">
    <div class="front-panel">
      <svg class="decor" viewBox="0 0 800 448" aria-hidden="true">
        <circle cx="800" cy="20" r="150" fill="none" stroke="var(--ring)" stroke-width="80"/>
        <circle cx="-20" cy="470" r="185" fill="none" stroke="var(--ring)" stroke-width="80"/>
      </svg>
      <div class="wordmark wordmark--front">
        <span class="wordmark-line1">Bluestone</span>
        <span class="wordmark-line2">Advisory &amp; Mgmt</span>
      </div>
    </div>
  </section>

  <section class="card card--back">
    <svg class="decor" viewBox="0 0 864 512" aria-hidden="true">
      <defs>
        <linearGradient id="swoosh" x1="0" y1="1" x2="1" y2="0">
          <stop offset="0" stop-color="var(--green-dark)"/>
          <stop offset="1" stop-color="var(--green-light)"/>
        </linearGradient>
      </defs>
      <circle cx="740" cy="172" r="158" fill="none" stroke="var(--ring)" stroke-width="82"/>
      <path d="M193,512 C480,470 740,270 864,0 L864,512 Z" fill="url(#swoosh)"/>
    </svg>

    <div class="holder">
      <h1 class="holder-name">DORIAN PELKEY</h1>
      <p class="holder-title">PRINCIPLE</p>
    </div>

    <ul class="contact-list">
      <li class="contact-item">
        <span class="contact-icon"><svg viewBox="0 0 24 24"><path d="M6.6 10.8a15.1 15.1 0 0 0 6.6 6.6l2.2-2.2c.3-.3.7-.4 1-.2 1.1.4 2.3.6 3.6.6.6 0 1 .4 1 1V20c0 .6-.4 1-1 1A17 17 0 0 1 3 4c0-.6.4-1 1-1h3.5c.6 0 1 .4 1 1 0 1.3.2 2.5.6 3.6.1.3 0 .7-.2 1z"/></svg></span>
        <span class="contact-text">917.806.3971</span>
      </li>
      <li class="contact-item">
        <span class="contact-icon"><svg viewBox="0 0 24 24"><path d="M2 6h20v1.2l-10 6.3L2 7.2z"/><path d="M2 9.4l10 6.3 10-6.3V19H2z"/></svg></span>
        <span class="contact-text">dorian@bam-hvx.example</span>
      </li>
      <li class="contact-item">
        <span class="contact-icon"><svg viewBox="0 0 24 24"><path d="M12 2a7 7 0 0 0-7 7c0 5 7 13 7 13s7-8 7-13a7 7 0 0 0-7-7zm0 9.5A2.5 2.5 0 1 1 12 6.5a2.5 2.5 0 0 1 0 5z"/></svg></span>
        <span class="contact-text">Website: bam-hvx.example</span>
      </li>
      <li class="contact-item">
        <span class="contact-icon"><svg viewBox="0 0 24 24"><path d="M12 2a10 10 0 1 0 0 20 10 10 0 0 0 0-20zm-1 2.1V8H7.6A8 8 0 0 1 11 4.1zm2 0A8 8 0 0 1 16.4 8H13zM4.6 10H11v4H4.6a8 8 0 0 1 0-4zm8.4 0h6.4a8 8 0 0 1 0 4H13zM7.6 16H11v3.9A8 8 0 0 1 7.6 16zm5.4 0h3.4a8 8 0 0 1-3.4 3.9z"/></svg></span>
        <span class="contact-text">348 West 71st Street, 9th FL<br>New York, NY 10010</span>
      </li>
    </ul>

    <div class="wordmark wordmark--back">
      <span class="wordmark-line1">Bluestone</span>
      <span class="wordmark-line2">Advisory &amp; Mgmt</span>
    </div>
  </section>

</div>
</body>
</html>
```